Business Card

Designs by L&M Renata Kowalczyk Signature Collection business card
Looking for a modern, classic and timeless business card for our jewelry company

Front of card should be a, all purple solid color for the background and white lettering like the attached document.

On the front of card:
Designs by L&M
Renata Kowalczyk Signature Collection
One of A Kind Designs for you!

Renata Fairbury
Owner

On the back on card
Email: LMDesigns27@postvela.com
Facebook: https://www.facepage-example.com/DesignsbyLMRenataandHolly
Twitter:
https://chirpline-example.com/DesignsbyLM27
Instagram: http://picstream-example.com/DesignsbyLMjewelry

Industry/Entity Type

Business

```html
<!DOCTYPE html>
<html lang="en">
<head>
<meta charset="utf-8">
<title>Designs by L&amp;M – Business Card</title>
<link rel="stylesheet" href="https://fonts.googleapis.com/css2?family=Questrial&family=Arimo:wght@400;700&display=swap">
<style>
  :root {
    --backdrop: #d6d6d9;
    --card-purple: #704a9f;
    --card-charcoal: #2d2b2c;
    --ink-white: #ffffff;
    --ink-grey: #d9d9d9;
    --mark-grey: #a3a3a3;
  }
  * { box-sizing: border-box; margin: 0; padding: 0; }
  html, body { width: 1200px; height: 960px; overflow: hidden; }
  body {
    background: var(--backdrop);
    display: flex;
    flex-direction: column;
    align-items: center;
    justify-content: center;
    gap: 40px;
    font-family: "Arimo", Arial, sans-serif;
  }
  .card {
    width: 735px;
    height: 420px;
    display: flex;
    flex-direction: column;
    align-items: center;
    box-shadow: 0 6px 18px rgba(0,0,0,0.25);
    color: var(--ink-white);
    text-align: center;
  }
  .card--front { background: var(--card-purple); padding-top: 58px; }
  .card--back { background: var(--card-charcoal); padding-top: 40px; }

  .brand-dot {
    width: 64px; height: 64px; border-radius: 50%;
    background: var(--ink-white);
    margin-bottom: 22px;
  }
  .card--back .brand-dot { width: 54px; height: 54px; background: var(--mark-grey); margin-bottom: 16px; }

  .brand-name {
    font-family: "Questrial", "Century Gothic", sans-serif;
    font-weight: 400;
    text-transform: uppercase;
    letter-spacing: 0.32em;
    font-size: 38px;
    line-height: 1;
    margin-right: -0.32em;
  }
  .card--back .brand-name { font-size: 25px; color: var(--ink-grey); }

  .brand-collection {
    font-family: "Questrial", "Century Gothic", sans-serif;
    font-size: 25px;
    margin-top: 6px;
  }
  .card--back .brand-collection { font-size: 16px; color: var(--ink-grey); margin-top: 4px; }

  .tagline { font-size: 16px; margin-top: 34px; }
  .owner-name { font-weight: 700; font-size: 17px; margin-top: 22px; }
  .owner-role { font-size: 16px; margin-top: 3px; }

  .contact-list {
    list-style: none;
    margin-top: 44px;
    display: flex;
    flex-direction: column;
    align-items: center;
    gap: 30px;
  }
  .contact-item {
    display: flex; align-items: center; gap: 10px;
    font-weight: 700; font-size: 15px; color: var(--ink-white);
  }
  .contact-icon { width: 24px; height: 24px; flex: none; }
  .contact-dot {
    width: 22px; height: 22px; border-radius: 50%;
    background: var(--mark-grey); flex: none;
  }
</style>
</head>
<body>
  <section class="card card--front" aria-label="Card front">
    <span class="brand-dot" aria-hidden="true"></span>
    <h1 class="brand-name">Designs by L&amp;M</h1>
    <p class="brand-collection">Renata Kowalczyk Signature Collection</p>
    <p class="tagline">One of A Kind Designs for you!</p>
    <p class="owner-name">Renata Fairbury</p>
    <p class="owner-role">Owner</p>
  </section>

  <section class="card card--back" aria-label="Card back">
    <span class="brand-dot" aria-hidden="true"></span>
    <h2 class="brand-name">Designs by L&amp;M</h2>
    <p class="brand-collection">Renata Kowalczyk Signature Collection</p>
    <ul class="contact-list">
      <li class="contact-item">
        <svg class="contact-icon" viewBox="0 0 24 24" aria-hidden="true">
          <rect x="1" y="5" width="22" height="14" fill="var(--mark-grey)"/>
          <path d="M1 5 L12 13 L23 5 M1 19 L9 11 M23 19 L15 11" stroke="var(--card-charcoal)" stroke-width="1.5" fill="none"/>
        </svg>
        LMDesigns27@postvela.com
      </li>
      <li class="contact-item">
        <span class="contact-dot" aria-hidden="true"></span>
        https://www.facepage-example.com/DesignsbyLMRenataandHolly
      </li>
      <li class="contact-item">
        <span class="contact-dot" aria-hidden="true"></span>
        https://chirpline-example.com/DesignsbyLM27
      </li>
      <li class="contact-item">
        <span class="contact-dot" aria-hidden="true"></span>
        http://picstream-example.com/DesignsbyLMjewelry
      </li>
    </ul>
  </section>
</body>
</html>
```